Need help in designing new business card utilizing our new logo.

BuildMarq Solutions works with Construction Business Owners, Managers & IT Professionals to strengthen software usage and increase user productivity.

Our Construction Accounting and Mobile Field Management Software Clients engage with us in the following areas:

New Software Implementations
Software Re-Implementations
Redesigning Software Usage at the User Level
Project Coordination & Management
Continued Software Support

Old tag line:
Weighing Options - Implementing Solutions

www.buildmarq-solutions.example

Stride 4 is a product, but not needed for a new business card.

```html
<!DOCTYPE html>
<html lang="en">
<head>
<meta charset="utf-8">
<title>BuildMarq Solutions – Business Card</title>
<link rel="stylesheet" href="https://fonts.googleapis.com/css2?family=Open+Sans:wght@400;600&family=Roboto+Condensed:wght@400&display=swap">
<style>
  :root {
    --brand-blue: #0a18a0;
    --card-grey: #c6c7cb;
    --hex-white: #f7f5f6;
    --ghost: #c9c6dc;
    --page-bg: #eceef2;
    --text-white: #ffffff;
  }
  html, body {
    margin: 0;
    padding: 0;
    overflow: hidden;
  }
  body {
    width: 1200px;
    height: 1042px;
    background: var(--page-bg);
    position: relative;
  }
  .card {
    position: absolute;
    width: 620px;
    height: 384px;
    box-shadow: 0 6px 18px rgba(0,0,0,0.18);
  }
  .card svg { display: block; width: 100%; height: 100%; }
  .card--front { left: 60px; top: 80px; }
  .card--back { left: 520px; top: 570px; }

  .front-text { font-family: "Open Sans", sans-serif; fill: var(--text-white); }
  .holder-name { font-size: 24px; font-weight: 600; }
  .holder-title { font-size: 19px; font-weight: 400; }
  .contact-line { font-size: 17px; font-weight: 400; }
  .brand-name { font-family: "Open Sans", sans-serif; font-size: 21px; font-weight: 600; fill: var(--brand-blue); }
  .brand-ghost { font-family: "Open Sans", sans-serif; font-size: 21px; font-weight: 600; fill: var(--ghost); }
  .service-label { font-family: "Roboto Condensed", sans-serif; font-size: 15.5px; fill: var(--brand-blue); text-anchor: end; }
  .service-icon circle.badge { fill: var(--brand-blue); }
  .glyph { fill: none; stroke: var(--text-white); stroke-width: 3; stroke-linecap: round; stroke-linejoin: round; }
  .glyph-fill { fill: var(--text-white); }
</style>
</head>
<body>

<div class="card card--front">
  <svg viewBox="0 0 653 404" xmlns="http://www.w3.org/2000/svg">
    <rect class="card-grey-field" x="0" y="0" width="653" height="404" fill="var(--card-grey)"/>
    <rect class="card-blue-field" x="0" y="0" width="456" height="404" fill="var(--brand-blue)"/>
    <polygon class="brand-hexagon" points="286,101 456,2 628,101 628,301 456,402 286,301" fill="var(--hex-white)"/>

    <text class="front-text holder-name" x="32" y="73">DANIEL REYES</text>
    <text class="front-text holder-title" x="30" y="95">Managing Director</text>

    <text class="front-text contact-line" x="32" y="189">480, Harbor Lane Suite 2</text>
    <text class="front-text contact-line" x="32" y="213">Northfield,</text>
    <text class="front-text contact-line" x="32" y="237">560210.</text>

    <path class="glyph-fill" d="M34 268 q7 -6 14 0 l0 3 l-3 0 l-1 -2 q-3 -1 -6 0 l-1 2 l-3 0 z M37 272 h8 l2 6 h-12 z"/>
    <text class="front-text contact-line" x="54" y="281">044-555 010 200</text>
    <rect x="37" y="290" width="8" height="13" rx="1.5" fill="none" stroke="var(--text-white)" stroke-width="2"/>
    <text class="front-text contact-line" x="54" y="305">044-555 010 200</text>
    <rect x="34" y="318" width="14" height="10" fill="var(--text-white)"/>
    <path d="M34 318 l7 6 l7 -6" fill="none" stroke="var(--brand-blue)" stroke-width="1.4"/>
    <text class="front-text contact-line" x="54" y="329">info@buildmarq.example</text>
    <circle cx="41" cy="347" r="6.5" fill="var(--text-white)"/>
    <path d="M36 345 h10 M36 349 h10 M41 341 v12" stroke="var(--brand-blue)" stroke-width="1.2"/>
    <text class="front-text contact-line" x="54" y="353">www.buildmarq-solutions.example</text>

    <g class="brand-lockup">
      <rect x="306" y="190" width="22" height="22" fill="var(--brand-blue)"/>
      <text class="brand-name" x="340" y="209" textLength="256" lengthAdjust="spacingAndGlyphs">BUILDMARQ SOLUTIONS</text>
    </g>
  </svg>
</div>

<div class="card card--back">
  <svg viewBox="0 0 653 404" xmlns="http://www.w3.org/2000/svg">
    <rect x="0" y="0" width="653" height="404" fill="var(--card-grey)"/>
    <rect x="0" y="0" width="206" height="404" fill="var(--brand-blue)"/>
    <polygon class="brand-hexagon" points="35,101 206,2 377,101 377,301 206,402 35,301" fill="var(--hex-white)"/>
    <text class="brand-ghost" x="78" y="209" textLength="256" lengthAdjust="spacingAndGlyphs">BUILDMARQ SOLUTIONS</text>

    <g class="service-list">
      <text class="service-label" x="556" y="57">PROJECT COORDINATION</text>
      <text class="service-label" x="556" y="77">MANAGEMENT</text>
      <g class="service-icon">
        <circle class="badge" cx="594" cy="61" r="31"/>
        <circle class="glyph-fill" cx="594" cy="50" r="6"/>
        <path class="glyph" d="M580 64 h28 M594 58 v20 M576 66 l4 -2 M612 66 l-4 -2"/>
        <circle class="glyph-fill" cx="574" cy="67" r="3"/>
        <circle class="glyph-fill" cx="614" cy="67" r="3"/>
        <circle class="glyph-fill" cx="594" cy="81" r="3"/>
      </g>

      <text class="service-label" x="556" y="126">NEW SOFTWARE</text>
      <text class="service-label" x="556" y="146">IMPLEMENTATIONS</text>
      <g class="service-icon">
        <circle class="badge" cx="594" cy="131" r="31"/>
        <rect class="glyph" x="592" y="116" width="16" height="26" rx="2"/>
        <circle class="glyph" cx="586" cy="136" r="8"/>
        <circle class="glyph-fill" cx="586" cy="136" r="2"/>
        <path class="glyph" d="M574 118 v8 M570 122 h8"/>
      </g>

      <text class="service-label" x="556" y="199">SOFTWARE</text>
      <text class="service-label" x="556" y="219">RE-IMPLEMENTATIONS</text>
      <g class="service-icon">
        <circle class="badge" cx="594" cy="204" r="31"/>
        <rect class="glyph" x="592" y="189" width="16" height="26" rx="2"/>
        <circle class="glyph" cx="586" cy="209" r="8"/>
        <circle class="glyph-fill" cx="586" cy="209" r="2"/>
        <path class="glyph" d="M574 196 a10 10 0 0 1 10 -6"/>
      </g>

      <text class="service-label" x="556" y="268">CONTINUED</text>
      <text class="service-label" x="556" y="288">SOFTWARE SUPPORT</text>
      <g class="service-icon">
        <circle class="badge" cx="594" cy="273" r="31"/>
        <path class="glyph" d="M579 275 v-4 a15 15 0 0 1 30 0 v4"/>
        <rect class="glyph-fill" x="575" y="271" width="7" height="11" rx="2"/>
        <rect class="glyph-fill" x="606" y="271" width="7" height="11" rx="2"/>
        <circle class="glyph-fill" cx="594" cy="268" r="6"/>
        <path class="glyph-fill" d="M584 290 q10 -16 20 0 z"/>
      </g>

      <text class="service-label" x="556" y="338">REDESIGNING SOFTWARE</text>
      <text class="service-label" x="556" y="358">USAGE AT THE USER LEVEL</text>
      <g class="service-icon">
        <circle class="badge" cx="594" cy="343" r="31"/>
        <circle class="glyph" cx="594" cy="343" r="9"/>
        <circle class="glyph-fill" cx="594" cy="343" r="3"/>
        <path class="glyph" d="M578 337 a17 17 0 0 1 22 -11 M610 349 a17 17 0 0 1 -22 11"/>
        <path class="glyph" d="M597 323 l4 3 l-4 3 M591 363 l-4 -3 l4 -3"/>
      </g>
    </g>
  </svg>
</div>

</body>
</html>
```